Website for Torvel Capital - investment banking firm

We have a corporate identity (thanks to Ranjita/41238) and want to extend that into a website design.  See the attached zipped files.
We have software folks in-house to do the coding.
See the attached Project Brief & Notes for more details.  Don't worry about the actual text - lorem ipsum will be fine.
The server will be Apache.
Thank you!
Desmond

```html
<!DOCTYPE html>
<html lang="en">
<head>
<meta charset="utf-8">
<title>Torvel Capital</title>
<link rel="stylesheet" href="https://fonts.googleapis.com/css2?family=Lato:wght@300;400;700&family=Open+Sans:wght@400;600;700&display=swap">
<style>
:root{
  --navy:#0e2a52;
  --navy-deep:#0a1f3e;
  --blue:#1f4f8f;
  --link-blue:#2257a0;
  --accent-red:#d7452f;
  --grey-card:#8e9297;
  --ink:#333a42;
  --muted:#6a7078;
  --team-bg:#141a22;
  --white:#ffffff;
  --line:#d9dde2;
}
*{box-sizing:border-box;margin:0;padding:0}
html,body{width:720px;height:1200px;overflow:hidden;background:var(--white)}
body{font-family:"Open Sans",Arial,sans-serif;color:var(--ink);position:relative}

.site-header{height:80px;background:var(--navy);position:relative}
.brand{position:absolute;left:60px;top:30px;display:flex;align-items:center;gap:7px;color:var(--white);font-family:"Lato",sans-serif;font-size:20px;font-weight:400;white-space:nowrap}
.brand-mark{width:20px;height:20px;border-radius:50%;background:var(--white)}
.contact-line{position:absolute;right:40px;top:5px;display:flex;gap:18px;font-size:8.5px;color:#c9d3e0}
.contact-line span{display:flex;align-items:center;gap:4px}
.main-nav{position:absolute;right:36px;top:30px;display:flex;height:30px}
.main-nav a{display:block;padding:0 8px;line-height:30px;font-size:8px;color:var(--white);text-decoration:none;letter-spacing:.2px;font-weight:600;white-space:nowrap}
.main-nav a.is-active{background:var(--blue);border-top:2px solid var(--accent-red);line-height:28px}

.hero{position:relative;height:280px;background:linear-gradient(100deg,#7d97b8 0%,#c8d6e6 35%,#e9eef4 55%,#5b6b80 80%,#2e3a4c 100%)}
.hero-arrow{position:absolute;top:120px;width:24px;height:36px}
.hero-arrow.prev{left:20px}.hero-arrow.next{right:20px}
.hero-dots{position:absolute;right:88px;bottom:14px;display:flex;gap:5px}
.hero-dots i{display:block;width:14px;height:3px;background:rgba(255,255,255,.7)}
.hero-dots i.on{background:var(--accent-red)}

.feature-cards{display:flex;gap:14px;padding:17px 67px 0 72px;height:163px}
.feature-card{display:flex;width:288px;height:146px}
.feature-photo{width:134px;height:146px;background:linear-gradient(135deg,#b6bcc4,#6d7580)}
.feature-body{flex:1;padding:14px 12px;color:var(--white)}
.feature-card.grey .feature-body{background:var(--grey-card)}
.feature-card.blue .feature-body{background:var(--blue)}
.feature-body h3{font-size:13px;font-weight:600;line-height:1.25;margin-bottom:6px}
.feature-body p{font-size:7px;line-height:1.45;opacity:.9;margin-bottom:8px}
.btn-ghost{display:inline-block;border:1px solid rgba(255,255,255,.8);font-size:6.5px;padding:3px 9px;color:var(--white);letter-spacing:.4px}

.section-title{font-family:"Lato",sans-serif;font-weight:300;font-size:30px;text-align:center;color:#2b3138}
.process{padding-top:20px;height:229px}
.process-grid{display:flex;justify-content:space-between;padding:12px 86px 0 86px}
.process-item{width:156px;text-align:center}
.process-icon{width:40px;height:40px;border-radius:50%;background:#3a3f46;margin:0 auto 9px;display:flex;align-items:center;justify-content:center}
.process-item h4{font-size:11px;font-weight:600;color:var(--link-blue);margin-bottom:4px;white-space:nowrap}
.process-item p{font-size:7px;line-height:1.5;color:var(--muted);text-align:left;margin-bottom:9px}
.btn-outline{display:inline-block;border:1px solid #9aa1a9;font-size:6.5px;padding:3px 10px;color:#555c64;letter-spacing:.4px}

.team{height:300px;background:linear-gradient(180deg,#1b232d,var(--team-bg));position:relative;color:var(--white)}
.team .section-title{color:var(--white);padding-top:22px}
.team-grid{display:flex;justify-content:space-between;padding:16px 96px 0}
.member{width:164px;text-align:center}
.member-photo{width:82px;height:82px;border-radius:50%;border:3px solid var(--white);margin:0 auto 8px;background:linear-gradient(160deg,#d8c4b0,#8a7462)}
.member h4{font-size:9.5px;font-weight:700;margin-bottom:3px;white-space:nowrap}
.member p{font-size:7px;line-height:1.45;color:#c9ced4;margin-bottom:7px}
.socials{display:flex;justify-content:center;gap:7px}
.socials i{display:block;width:8px;height:8px;border-radius:50%;background:#d0d5db}
.team-arrow{position:absolute;top:140px;width:20px;height:32px}
.team-arrow.prev{left:10px}.team-arrow.next{right:10px}

.clients{height:79px;padding-top:8px}
.clients .section-title{font-size:26px}
.client-row{display:flex;justify-content:space-between;align-items:center;padding:8px 74px 0}
.client-row span{font-family:"Open Sans",sans-serif;font-size:10px;font-weight:700;color:#7b8087;letter-spacing:.3px;display:flex;align-items:center;gap:3px}
.client-row b{display:block;width:9px;height:9px;border-radius:50%;background:#9ba0a6}
.site-footer{position:absolute;left:0;bottom:0;width:720px;height:29px;background:var(--navy-deep);color:#c4ccd6;font-size:8px;line-height:29px;padding-left:72px}
</style>
</head>
<body>

<header class="site-header">
  <div class="brand"><span class="brand-mark"></span>Torvel Capital</div>
  <div class="contact-line">
    <span><svg width="9" height="7" viewBox="0 0 9 7"><rect x=".5" y=".5" width="8" height="6" fill="none" stroke="#c9d3e0"/><path d="M.5 .5 4.5 4 8.5 .5" fill="none" stroke="#c9d3e0"/></svg>hello@torvelcapital.com</span>
    <span><svg width="7" height="9" viewBox="0 0 7 9"><rect x=".5" y=".5" width="6" height="8" rx="1" fill="none" stroke="#c9d3e0"/></svg>555.014.2290</span>
  </div>
  <nav class="main-nav">
    <a class="is-active" href="#">HOME</a>
    <a href="#">ABOUT</a>
    <a href="#">SERVICES</a>
    <a href="#">CURRENT ENGAGEMENTS</a>
    <a href="#">COMPLETED TRANSACTIONS</a>
  </nav>
</header>

<section class="hero" role="img" aria-label="Photo of business people reviewing documents at a meeting table">
  <svg class="hero-arrow prev" viewBox="0 0 24 36"><path d="M18 4 6 18l12 14" fill="none" stroke="#fff" stroke-width="3"/></svg>
  <svg class="hero-arrow next" viewBox="0 0 24 36"><path d="M6 4l12 14L6 32" fill="none" stroke="#fff" stroke-width="3"/></svg>
  <div class="hero-dots"><i class="on"></i><i></i><i></i></div>
</section>

<section class="feature-cards">
  <article class="feature-card grey">
    <div class="feature-photo" role="img" aria-label="Photo of colleagues in an office meeting"></div>
    <div class="feature-body">
      <h3>Lorem ipsum dolor sit amet,</h3>
      <p>consectetur adipiscing elit, sed do eiusmod tempor incididunt ut labore et dolore magna aliqua.</p>
      <span class="btn-ghost">READ MORE</span>
    </div>
  </article>
  <article class="feature-card blue">
    <div class="feature-photo" role="img" aria-label="Photo of a team working at a laptop"></div>
    <div class="feature-body">
      <h3>Lorem ipsum dolor sit amet,</h3>
      <p>consectetur adipiscing elit, sed do eiusmod tempor incididunt ut labore et dolore magna aliqua.</p>
      <span class="btn-ghost">READ MORE</span>
    </div>
  </article>
</section>

<section class="process">
  <h2 class="section-title">Our Process</h2>
  <div class="process-grid">
    <div class="process-item">
      <div class="process-icon"><svg width="20" height="20" viewBox="0 0 20 20"><circle cx="10" cy="10" r="8" fill="none" stroke="#fff" stroke-width="2"/><path d="M10 10V2a8 8 0 0 1 8 8z" fill="#fff"/></svg></div>
      <h4>Lorem ipsum dolor sit amet.</h4>
      <p>Lorem ipsum dolor sit amet, consectetur adipiscing elit, sed do eiusmod tempor incididunt ut labore et dolore magna aliqua.</p>
      <span class="btn-outline">READ MORE</span>
    </div>
    <div class="process-item">
      <div class="process-icon"><svg width="20" height="20" viewBox="0 0 20 20"><path d="M2 2v16h16" fill="none" stroke="#fff" stroke-width="1.6"/><path d="M4 14l4-5 3 3 5-7" fill="none" stroke="#fff" stroke-width="1.6"/></svg></div>
      <h4>Lorem ipsum dolor sit amet.</h4>
      <p>Lorem ipsum dolor sit amet, consectetur adipiscing elit, sed do eiusmod tempor incididunt ut labore et dolore magna aliqua.</p>
      <span class="btn-outline">READ MORE</span>
    </div>
    <div class="process-item">
      <div class="process-icon"><svg width="22" height="20" viewBox="0 0 22 20"><circle cx="7" cy="6" r="3" fill="#fff"/><circle cx="15" cy="6" r="3" fill="#fff"/><path d="M2 17a5 5 0 0 1 10 0zM10 17a5 5 0 0 1 10 0z" fill="#fff"/></svg></div>
      <h4>Lorem ipsum dolor sit amet.</h4>
      <p>Lorem ipsum dolor sit amet, consectetur adipiscing elit, sed do eiusmod tempor incididunt ut labore et dolore magna aliqua.</p>
      <span class="btn-outline">READ MORE</span>
    </div>
  </div>
</section>

<section class="team">
  <h2 class="section-title">Our Team</h2>
  <svg class="team-arrow prev" viewBox="0 0 20 32"><path d="M15 4 5 16l10 12" fill="none" stroke="#fff" stroke-width="3"/></svg>
  <svg class="team-arrow next" viewBox="0 0 20 32"><path d="M5 4l10 12L5 28" fill="none" stroke="#fff" stroke-width="3"/></svg>
  <div class="team-grid">
    <div class="member">
      <div class="member-photo" role="img" aria-label="Portrait photo of a team member"></div>
      <h4>Lorem ipsum dolor sit amet,</h4>
      <p>Lorem ipsum dolor sit amet, consectetur adipiscing elit, sed do eiusmod tempor incididunt.</p>
      <div class="socials"><i></i><i></i><i></i><i></i></div>
    </div>
    <div class="member">
      <div class="member-photo" role="img" aria-label="Portrait photo of a team member"></div>
      <h4>Lorem ipsum dolor sit amet,</h4>
      <p>Lorem ipsum dolor sit amet, consectetur adipiscing elit, sed do eiusmod tempor incididunt.</p>
      <div class="socials"><i></i><i></i><i></i><i></i></div>
    </div>
    <div class="member">
      <div class="member-photo" role="img" aria-label="Portrait photo of a team member"></div>
      <h4>Lorem ipsum dolor sit amet,</h4>
      <p>Lorem ipsum dolor sit amet, consectetur adipiscing elit, sed do eiusmod tempor incididunt.</p>
      <div class="socials"><i></i><i></i><i></i><i></i></div>
    </div>
  </div>
</section>

<section class="clients">
  <h2 class="section-title">Our Client</h2>
  <div class="client-row">
    <span>Rendal</span>
    <span><b></b>Corvo</span>
    <span>Harlow</span>
    <span>Stavern</span>
    <span>Nesto</span>
    <span>Pellam</span>
    <span><b></b>Ossel</span>
    <span>Brightway</span>
  </div>
</section>

<footer class="site-footer">All rights reserved © 2014. torvelcapital</footer>

</body>
</html>
```